ThePolicyPalNV General Postcard

My Insurance Agency - R. T. Hallorby Insurance Services Provides Insurance products to all of California. Most specifically the Bay Area.
"The Coverage Guy" is who I am advertising. providing Insurance solutions and consultations.
My Main Products are:
Life
Health
Disability
Accident
Employee Benefits
The colors of the card should match my uploaded logo.
I want the card to portray professionalism and security....Trust...and make people want to pick up the phone right now and make an appointment?
Young families, Seniors
Insurance

```html
<!DOCTYPE html>
<html lang="en">
<head>
<meta charset="utf-8">
<title>The Coverage Guy – Postcard</title>
<link href="https://fonts.googleapis.com/css2?family=EB+Garamond:wght@400;700&family=Arimo:wght@400&display=swap" rel="stylesheet">
<style>
  :root{
    --page:#262626;
    --card:#ffffff;
    --navy:#1c3163;
    --navy-deep:#0f2250;
    --navy-light:#2f5190;
    --sky:#93acd8;
    --headline-blue:#3b5b90;
    --ink:#222222;
    --label:#333333;
    --frame:#3a8fd0;
    --gold:#d7a824;
    --serif:"EB Garamond", Georgia, serif;
    --sans:"Arimo", Arial, sans-serif;
  }
  *{box-sizing:border-box;margin:0;padding:0}
  html,body{width:1200px;height:1200px;overflow:hidden;background:var(--page)}
  body{font-variant-numeric:lining-nums}
  .canvas{position:relative;width:1200px;height:1200px}
  .card{position:absolute;background:var(--card);overflow:hidden;box-shadow:0 2px 6px rgba(0,0,0,.4)}

  /* Mailing side */
  .card-back{left:419px;top:26px;width:727px;height:558px}
  .back-band{position:absolute;left:0;top:0}
  .products-title{position:absolute;left:19px;top:12px;font:400 31px/1 var(--serif);color:var(--ink)}
  .product{position:absolute;width:140px;text-align:center}
  .product-art{display:block;width:140px;height:73px;border:2px solid var(--frame);border-radius:7px;
    background:linear-gradient(180deg,#fafafa,#e6e6e6)}
  .product-name{display:block;margin-top:6px;font:16px/1.1 var(--sans);color:var(--label);white-space:nowrap;margin-left:-40px;margin-right:-40px}
  .product-life{left:18px;top:56px}
  .product-health{left:203px;top:56px}
  .product-disability{left:18px;top:162px}
  .product-accident{left:203px;top:162px}
  .product-benefits{left:112px;top:268px}
  .back-call{position:absolute;left:11px;top:410px;color:#fff;font-family:var(--serif);line-height:1.15}
  .back-call .call-line{font-size:17px;display:block}
  .back-call .phone{font-size:24px;display:block}
  .sender{position:absolute;left:366px;top:18px;font-family:var(--serif);font-style:normal;color:var(--ink)}
  .sender-name{font-size:19px;font-weight:700;display:block;line-height:1.2}
  .sender-line{font-size:13px;display:block;line-height:1.25}
  .sender-line.strong{font-weight:700}
  .stamp-box{position:absolute;left:551px;top:10px;width:166px;height:166px;border:1px solid #9a9a9a}

  /* Picture side */
  .card-front{left:64px;top:614px;width:729px;height:562px}
  .family-photo{position:absolute;left:0;top:130px;width:729px;height:432px;
    background:linear-gradient(180deg,#ffffff 0%,#efe7e2 20%,#d8b79e 50%,#b89a84 75%,#8f9fb5 100%)}
  .front-band{position:absolute;left:0;top:0}
  .brand{position:absolute;left:24px;top:74px;display:flex;align-items:center;gap:10px;
    font:400 26px/1 var(--serif);color:var(--navy)}
  .brand-mark{width:18px;height:18px;background:var(--navy)}
  .headline{position:absolute;left:260px;width:480px;text-align:center;font-family:var(--serif);font-weight:400;line-height:1}
  .headline-top{top:32px;font-size:29px;color:var(--ink)}
  .headline-main{top:68px;font-size:36px;color:var(--headline-blue)}
  .seal{position:absolute;left:576px;top:358px;width:108px;height:108px;border-radius:50%;
    background:radial-gradient(circle at 40% 35%,#f3d469,var(--gold) 60%,#a97c12);
    display:flex;flex-direction:column;align-items:center;justify-content:center;
    color:#fff;font-family:var(--serif);line-height:1;text-align:center}
  .seal-top{font-size:15px;letter-spacing:.5px}
  .seal-main{font-size:29px;margin:1px 0}
  .seal-bottom{font-size:9px;letter-spacing:.5px}
  .front-call{position:absolute;right:23px;top:484px;text-align:right;color:#fff;font-family:var(--serif);line-height:1.1}
  .front-call .call-line{font-size:24px;display:block}
  .front-call .phone{font-size:36px;display:block}
</style>
</head>
<body>
<main class="canvas">

  <section class="card card-back" aria-label="Postcard mailing side">
    <svg class="back-band" width="727" height="558" viewBox="0 0 727 558" aria-hidden="true">
      <defs>
        <linearGradient id="backNavy" x1="0" y1="0" x2="1" y2="0">
          <stop offset="0" stop-color="#0f2250"/>
          <stop offset="1" stop-color="#2f5190"/>
        </linearGradient>
      </defs>
      <path d="M0,306 C110,392 250,455 373,466 L0,466 Z" fill="var(--sky)"/>
      <path d="M0,320 C110,404 240,458 356,466 L0,466 Z" fill="url(#backNavy)"/>
    </svg>

    <h2 class="products-title">Our Products</h2>

    <div class="product product-life">
      <span class="product-art" role="img" aria-label="Illustration of a figure holding a red heart"></span>
      <span class="product-name">Life Insurance</span>
    </div>
    <div class="product product-health">
      <span class="product-art" role="img" aria-label="Illustration of a figure with a stethoscope"></span>
      <span class="product-name">Health Insurance</span>
    </div>
    <div class="product product-disability">
      <span class="product-art" role="img" aria-label="Illustration of a figure on crutches"></span>
      <span class="product-name">Disability Insurance</span>
    </div>
    <div class="product product-accident">
      <span class="product-art" role="img" aria-label="Illustration of two figures carrying a stretcher"></span>
      <span class="product-name">Accident Insurance</span>
    </div>
    <div class="product product-benefits">
      <span class="product-art" role="img" aria-label="Illustration of a team of figures with one in red"></span>
      <span class="product-name">Employee Benefits Insurance</span>
    </div>

    <p class="back-call"><span class="call-line">Call Us Today!</span><span class="phone">(000) 000-0000</span></p>

    <address class="sender">
      <span class="sender-name">R. T. Hallorby</span>
      <span class="sender-line strong">Insurance Services</span>
      <span class="sender-line">Your Address Here</span>
    </address>

    <div class="stamp-box" aria-label="Stamp area"></div>
  </section>

  <section class="card card-front" aria-label="Postcard picture side">
    <div class="family-photo" role="img" aria-label="Photo of a smiling young family lying together on a soft white rug"></div>

    <svg class="front-band" width="729" height="562" viewBox="0 0 729 562" aria-hidden="true">
      <defs>
        <linearGradient id="frontNavy" x1="0" y1="1" x2="1" y2="0">
          <stop offset="0" stop-color="#0f2250"/>
          <stop offset="1" stop-color="#2f5190"/>
        </linearGradient>
      </defs>
      <path d="M240,562 C450,520 640,410 729,196 L729,562 Z" fill="var(--sky)"/>
      <path d="M278,562 C470,526 650,432 729,222 L729,562 Z" fill="url(#frontNavy)"/>
    </svg>

    <div class="brand"><span class="brand-mark"></span><span>The Coverage Guy</span></div>

    <p class="headline headline-top">Providing Insurance</p>
    <h1 class="headline headline-main">Solutions and Consultations</h1>

    <div class="seal" aria-label="Risk free guarantee seal">
      <span class="seal-top">RISK</span>
      <span class="seal-main">FREE</span>
      <span class="seal-bottom">GUARANTEE</span>
    </div>

    <p class="front-call"><span class="call-line">Call Us Today!</span><span class="phone">(000) 000-0000</span></p>
  </section>

</main>
</body>
</html>
```